Mobile app for deals

Mobile App Name: Vanta 6 Mirk

Design screen shots for the issue of quotes for deals.

1. Loading screen
2. User signs in with credentials or signs up
2. Search by category
3. Search by location
4. Create a project

The expected experience after a project is placed:
- Project alerted
- Quotes
- Project complete
- Rating
- Payment

#TotallyExcited
Updates

Project Deadline Extended Reason: Deadline has been extended on request from a few designers who saw the project late and who would like to submit designs.Thank you to all who submitted on time, we are reviewing your designs and will respond shortly. Added Monday, June 29, 2015

Target Market(s)

Contractors market

Industry/Entity Type

Business Directory

Font styles to use
Sans Serif

Requirements
Must have
• Simple design
• User friendly
• Translateable (later)

```html
<!DOCTYPE html>
<html lang="en">
<head>
<meta charset="utf-8">
<title>Vanta 6 Mirk – Looking for a professional</title>
<link href="https://fonts.googleapis.com/css2?family=Lato:wght@400;700&display=swap" rel="stylesheet">
<style>
  :root {
    --page-bg: #2b2e36;
    --screen-bg: #2f2f2f;
    --header-bg: #2d2d2d;
    --photo-top: #6b5a3a;
    --photo-mid: #8a3b4a;
    --photo-low: #3c4a2c;
    --scrim: rgba(20, 20, 22, 0.78);
    --signin: #1d4f7a;
    --register: #6c9a1e;
    --modal-bg: #ffffff;
    --ink: #2a2a2a;
    --bulb: #f5e53a;
  }
  * { box-sizing: border-box; margin: 0; padding: 0; }
  html, body {
    width: 1200px; height: 1139px; overflow: hidden;
    background: var(--page-bg);
    font-family: "Lato", "Helvetica Neue", Arial, sans-serif;
  }
  .screen {
    position: absolute; left: 320px; top: 72px;
    width: 560px; height: 994px;
    background: var(--screen-bg);
    overflow: hidden;
  }
  .app-header {
    position: absolute; left: 0; top: 0; width: 100%; height: 120px;
    background: var(--header-bg);
  }
  .hero-photo {
    position: absolute; left: 0; top: 120px; width: 100%; height: 874px;
    background: linear-gradient(160deg, var(--photo-top) 0%, var(--photo-mid) 45%, var(--photo-low) 100%);
  }
  .auth-actions {
    position: absolute; left: 28px; right: 28px; bottom: 120px;
    display: flex; gap: 24px;
  }
  .auth-button {
    flex: 1; height: 84px; border-radius: 6px;
    display: flex; align-items: center; justify-content: center;
    color: #fff; font-size: 24px; letter-spacing: 2px; text-transform: uppercase;
  }
  .auth-button--signin { background: var(--signin); }
  .auth-button--register { background: var(--register); }
  .scrim { position: absolute; inset: 0; background: var(--scrim); }
  .info-modal {
    position: absolute; left: 40px; top: 170px; width: 480px; height: 600px;
    background: var(--modal-bg); border-radius: 4px;
    padding: 0 44px;
  }
  .info-modal__close {
    position: absolute; right: 22px; top: 20px; width: 26px; height: 26px;
  }
  .info-modal__icon { display: block; margin: 96px auto 0; width: 150px; height: 200px; }
  .info-modal__title {
    margin-top: 34px; font-size: 34px; font-weight: 400; color: var(--ink); text-align: center;
  }
  .steps {
    list-style: none; margin-top: 22px; color: var(--ink);
    font-size: 22px; line-height: 36px;
  }
</style>
</head>
<body>
  <main class="screen">
    <div class="app-header"></div>
    <div class="hero-photo" role="img" aria-label="Photo of contractors at work behind the welcome screen"></div>
    <div class="auth-actions">
      <div class="auth-button auth-button--signin">Sign in</div>
      <div class="auth-button auth-button--register">Register</div>
    </div>
    <div class="scrim"></div>

    <section class="info-modal" aria-labelledby="modal-title">
      <svg class="info-modal__close" viewBox="0 0 26 26" aria-label="Close">
        <path d="M4 4 L22 22 M22 4 L4 22" stroke="#333" stroke-width="2.4" stroke-linecap="round"/>
      </svg>
      <svg class="info-modal__icon" viewBox="0 0 150 200" aria-hidden="true">
        <g fill="none" stroke="var(--bulb)" stroke-width="7" stroke-linejoin="round" stroke-linecap="round">
          <path d="M50 140 C45 115 10 100 10 65 A65 65 0 0 1 140 65 C140 100 105 115 100 140 Z"/>
          <path d="M48 140 H102 V156 H48 Z"/>
          <path d="M52 156 H98 V170 Q98 178 90 178 H60 Q52 178 52 170 Z"/>
          <path d="M64 178 Q75 194 86 178"/>
        </g>
      </svg>
      <h1 class="info-modal__title" id="modal-title">Looking for a professional</h1>
      <ol class="steps">
        <li>1. Sign in and create a profile.</li>
        <li>2. Place a project for free.</li>
        <li>3. Recieve quotes for the project.</li>
        <li>4. Review professional's profiles.</li>
        <li>5. Select a professional for the work.</li>
      </ol>
    </section>
  </main>
</body>
</html>
```